New Bicycle shop business card

Hi!
I'm looking for a business card for my new proffesional bike mechanics shop. This shop is only for fixing broken bikes and not selling bikes.
Peferbly a modern and sleek and modern design.
Colors: black, grey, red, white
Information:
Name: Rijwielwerkplaats Vanhoutem
Shop owner: Bart Vanhoutem & Sanne Maertens
Website: www.rijwielwerkplaats-vanhoutem.be
Email: info@rijwielwerkplaats-vanhoutem.be
Phone number: +32471902386
Street adres: Kerkweg 64
9970 Oostmoere
Slogan/shop information: Herstellingen van alle merken.
Logo: see files.
Target Market(s)
People who seek a mechanic to fix or upgrade their bikes.
Contact Information for Business Card
Information:
Website: info@rijwielwerkplaats-vanhoutem.be
9970 Oostmoere
Logo: see files.

```html
<!DOCTYPE html>
<html lang="nl">
<head>
<meta charset="utf-8">
<title>Rijwielwerkplaats Vanhoutem – Visitekaartje</title>
<link href="https://fonts.googleapis.com/css2?family=Montserrat:wght@500;700&display=swap" rel="stylesheet">
<style>
  :root {
    --bg: #2b2b2d;
    --red: #e01e3c;
    --white: #ffffff;
    --black: #1a1414;
    --grey: #a9a9a9;
  }
  * { margin: 0; padding: 0; box-sizing: border-box; }
  html, body { width: 1200px; height: 880px; overflow: hidden; }
  body {
    background: var(--bg);
    font-family: "Montserrat", Arial, sans-serif;
    position: relative;
  }
  .card {
    position: absolute;
    width: 560px;
    height: 362px;
    border-radius: 22px;
    box-shadow: 0 10px 28px rgba(0,0,0,.45);
    overflow: hidden;
  }
  /* Front */
  .card-front {
    left: 90px; top: 60px;
    background: var(--red);
    color: var(--white);
    display: flex; flex-direction: column; align-items: center; justify-content: center;
    text-align: center;
  }
  .front-mark {
    width: 46px; height: 46px;
    background: var(--white);
    margin-bottom: 18px;
  }
  .front-name {
    font-weight: 700;
    font-size: 26px;
    letter-spacing: 2px;
    line-height: 1.2;
    text-transform: uppercase;
  }
  .front-name .spaced { letter-spacing: 9px; }
  .front-tagline {
    margin-top: 16px;
    font-weight: 500;
    font-size: 15px;
    letter-spacing: 1.5px;
  }
  /* Back */
  .card-back {
    left: 550px; top: 458px;
    background: var(--white);
    color: var(--black);
  }
  .back-name {
    position: absolute; left: 36px; top: 130px;
    font-weight: 700;
    font-size: 22px;
    letter-spacing: 1px;
    line-height: 1.2;
    text-transform: uppercase;
    color: var(--black);
  }
  .back-name .spaced { letter-spacing: 7px; }
  .back-mark {
    position: absolute; right: 50px; top: 40px;
    width: 150px; height: 150px;
    border-radius: 50%;
    background: var(--red);
  }
  .owners {
    position: absolute; left: 36px; top: 202px;
    font-weight: 500; font-size: 13px;
    text-transform: uppercase; letter-spacing: .3px;
  }
  .contact-list {
    position: absolute; left: 36px; top: 232px;
    list-style: none;
  }
  .contact-item {
    display: flex; align-items: center; gap: 10px;
    font-size: 12.5px; font-weight: 500;
    height: 25px;
  }
  .contact-icon {
    width: 18px; height: 18px; flex: none;
  }
</style>
</head>
<body>

  <section class="card card-front" aria-label="Voorkant visitekaartje">
    <div class="front-mark"></div>
    <h1 class="front-name">Rijwielwerkplaats<br><span class="spaced">Vanhoutem</span></h1>
    <p class="front-tagline">Herstellingen Van Alle Merken</p>
  </section>

  <section class="card card-back" aria-label="Achterkant visitekaartje">
    <div class="back-mark"></div>
    <h2 class="back-name">Rijwielwerkplaats<br><span class="spaced">Vanhoutem</span></h2>
    <p class="owners">Bart Vanhoutem &amp; Sanne Maertens</p>
    <ul class="contact-list">
      <li class="contact-item">
        <svg class="contact-icon" viewBox="0 0 20 20" aria-hidden="true"><circle cx="10" cy="10" r="10" fill="#e01e3c"/><path d="M7 5.5l2 2.2-1 1.2c.6 1.3 1.6 2.3 2.9 2.9l1.2-1 2.2 2-1 1.4c-3.6-.4-6.4-3.2-6.8-6.8z" fill="#fff"/></svg>
        +32471902386
      </li>
      <li class="contact-item">
        <svg class="contact-icon" viewBox="0 0 20 20" aria-hidden="true"><circle cx="10" cy="10" r="10" fill="#e01e3c"/><rect x="5" y="6.5" width="10" height="7" fill="none" stroke="#fff" stroke-width="1.3"/><path d="M5 6.5l5 4 5-4" fill="none" stroke="#fff" stroke-width="1.3"/></svg>
        info@rijwielwerkplaats-vanhoutem.be
      </li>
      <li class="contact-item">
        <svg class="contact-icon" viewBox="0 0 20 20" aria-hidden="true"><circle cx="10" cy="10" r="10" fill="#e01e3c"/><circle cx="10" cy="10" r="5" fill="none" stroke="#fff" stroke-width="1.2"/><ellipse cx="10" cy="10" rx="2.2" ry="5" fill="none" stroke="#fff" stroke-width="1.1"/><path d="M5 10h10" stroke="#fff" stroke-width="1.1"/></svg>
        www.rijwielwerkplaats-vanhoutem.be
      </li>
      <li class="contact-item">
        <svg class="contact-icon" viewBox="0 0 20 20" aria-hidden="true"><circle cx="10" cy="10" r="10" fill="#e01e3c"/><path d="M10 15.5s-4-4.2-4-7a4 4 0 018 0c0 2.8-4 7-4 7z" fill="#fff"/><circle cx="10" cy="8.5" r="1.5" fill="#e01e3c"/></svg>
        Kerkweg 64, 9970 Oostmoere
      </li>
    </ul>
  </section>

</body>
</html>
```